RivoCounsel Compensation Lawyers

We need a modern, sleek letterhead that is professional.

In relation to the footer, we would like to have firm contact details there ideally, however you must also insert at the bottom of each page the following....

Liability limited by a scheme approved under the Professional Standards Legislation.

From the attachment you can extract the firm logo. Also, I would like the Accredited specialist circle on the letterhead also.

Also, I would like you to create a document that can easily be edited for change of contact details, as these are likely to change.

Industry/Entity Type

It Professional

Font styles to use
Sans Serif

Colors
0655a3
3276b5
85abd2
0492cd
33a6d7
85cae6
cee9f5
eaf1f7
cbcbcb

Requirements
Must have
• Ph: 8371-5264
• F: 8815-3927
• M 0468-253-914
• mk@rivocounsel.example.au
• www.rivocounsel.example.au
Nice to have
• the word document gives you an idea of what I like. I am happy for your to amaze me with your creativity.

```html
<!DOCTYPE html>
<html lang="en">
<head>
<meta charset="utf-8">
<title>RivoCounsel Compensation Lawyers – Letterhead</title>
<link rel="stylesheet" href="https://fonts.googleapis.com/css2?family=Carlito:wght@400;700&display=swap">
<style>
  :root {
    --navy: #0655a3;
    --blue: #3276b5;
    --sky: #0492cd;
    --sky-light: #33a6d7;
    --pale: #85cae6;
    --rule: #cbcbcb;
    --paper: #f2f2f0;
    --backdrop: #e2e2e2;
    --ink-dark: #1c2430;
  }
  * { margin: 0; padding: 0; box-sizing: border-box; }
  html, body {
    width: 1113px;
    height: 1200px;
    overflow: hidden;
    background: var(--backdrop);
    font-family: "Carlito", "Calibri", Arial, sans-serif;
  }
  .letterhead {
    position: absolute;
    left: 210px;
    top: 97px;
    width: 760px;
    height: 1018px;
    background: var(--paper);
  }
  .brand {
    position: absolute;
    left: 46px;
    top: 62px;
    display: flex;
    align-items: center;
    gap: 10px;
  }
  .brand-dot {
    width: 26px;
    height: 26px;
    border-radius: 50%;
    background: var(--sky-light);
  }
  .brand-name {
    font-weight: 700;
    font-size: 17px;
    letter-spacing: 0.2px;
    color: var(--navy);
    text-transform: uppercase;
    white-space: nowrap;
  }
  .office {
    position: absolute;
    left: 412px;
    top: 75px;
    font-size: 10.5px;
    line-height: 13.6px;
    color: var(--blue);
  }
  .office-title { font-weight: 700; color: var(--navy); }
  .office-web { color: var(--navy); }
  .contact-divider {
    position: absolute;
    left: 566px;
    top: 74px;
    width: 2px;
    height: 55px;
    background: var(--navy);
  }
  .contacts {
    position: absolute;
    left: 574px;
    top: 75px;
    font-size: 10.5px;
    line-height: 13.6px;
    list-style: none;
  }
  .contacts li { display: flex; }
  .contacts .label { width: 20px; color: var(--navy); }
  .contacts .value { color: var(--sky); }
  .header-rule {
    position: absolute;
    left: 45px;
    top: 137px;
    width: 671px;
    height: 2px;
    background: var(--rule);
  }
  .practice-areas {
    position: absolute;
    left: 150px;
    top: 930px;
    width: 450px;
    text-align: center;
    font-size: 14px;
    color: var(--navy);
    white-space: nowrap;
  }
  .footer-rule {
    position: absolute;
    left: 150px;
    top: 952px;
    width: 450px;
    height: 3px;
  }
  .liability {
    position: absolute;
    left: 150px;
    top: 960px;
    width: 450px;
    text-align: center;
    font-size: 11px;
    color: var(--blue);
    white-space: nowrap;
  }
  .accreditation-badge {
    position: absolute;
    left: 601px;
    top: 922px;
    width: 60px;
    height: 60px;
  }
</style>
</head>
<body>
  <main class="letterhead">
    <header>
      <div class="brand">
        <span class="brand-dot"></span>
        <span class="brand-name">RivoCounsel Compensation Lawyers</span>
      </div>

      <address class="office" style="font-style: normal;">
        <div class="office-title">Harbourview Office</div>
        <div>P.O. Box B418 Kelmont</div>
        <div>South NSW 2190</div>
        <div class="office-web">www.rivocounsel.example.au</div>
      </address>

      <div class="contact-divider"></div>

      <ul class="contacts">
        <li><span class="label">P:</span><span class="value">8371-5264</span></li>
        <li><span class="label">F:</span><span class="value">8815-3927</span></li>
        <li><span class="label">M:</span><span class="value">0468-253-914</span></li>
        <li><span class="label">E:</span><span class="value">mk@rivocounsel.example.au</span></li>
      </ul>

      <div class="header-rule"></div>
    </header>

    <footer>
      <div class="practice-areas">Insurance Law | Estate &amp; Property Law | Family Law | Commercial Law</div>
      <svg class="footer-rule" viewBox="0 0 450 3" preserveAspectRatio="none">
        <defs>
          <linearGradient id="footerRuleFade" x1="0" x2="1" y1="0" y2="0">
            <stop offset="0" stop-color="#0655a3" stop-opacity="0.15"/>
            <stop offset="0.25" stop-color="#0655a3"/>
            <stop offset="1" stop-color="#0655a3"/>
          </linearGradient>
        </defs>
        <rect x="0" y="0.5" width="450" height="2" fill="url(#footerRuleFade)"/>
      </svg>
      <div class="liability">Liability limited by a scheme approved under Professional Standards Legislation</div>
      <svg class="accreditation-badge" viewBox="0 0 60 60" role="img" aria-label="Specialist accreditation badge">
        <circle cx="30" cy="30" r="28" fill="#1c2430"/>
        <circle cx="30" cy="30" r="19" fill="#0492cd"/>
      </svg>
    </footer>
  </main>
</body>
</html>
```